Shaker Barons business card

We would like a business card designed for our business shaker barons

We need it to have 2 sides.

More information about the business can be found at www.shakerbarons.net

```html
<!DOCTYPE html>
<html lang="en">
<head>
<meta charset="utf-8">
<title>Shaker Barons business card</title>
<link href="https://fonts.googleapis.com/css2?family=Poiret+One&display=swap" rel="stylesheet">
<style>
  :root {
    --page-bg: #e9e6e1;
    --card-white: #fbfaf7;
    --gold: #c9a43f;
    --ink-grey: #6f6a64;
    --light: #ffffff;
    --bar-dark: #2a1714;
    --bar-red: #9e2a33;
    --bar-amber: #c9783a;
  }
  * { margin: 0; padding: 0; box-sizing: border-box; }
  html, body {
    width: 1200px; height: 1000px; overflow: hidden;
    background: var(--page-bg);
    font-family: "Poiret One", sans-serif;
  }
  .card {
    position: absolute;
    left: 250px;
    width: 700px; height: 400px;
    overflow: hidden;
    box-shadow: 0 6px 18px rgba(0,0,0,0.18);
  }
  .card--front { top: 70px; background: var(--card-white); }
  .card--back { top: 530px; }

  .bar-photo {
    position: absolute;
    background:
      radial-gradient(ellipse at 30% 40%, rgba(220,235,210,0.55), transparent 35%),
      radial-gradient(ellipse at 75% 30%, rgba(201,120,58,0.7), transparent 45%),
      linear-gradient(160deg, var(--bar-amber) 0%, var(--bar-red) 45%, var(--bar-dark) 100%);
  }
  .card--front .bar-photo { left: 0; right: 0; bottom: 0; height: 150px; }
  .card--back .bar-photo { inset: 0; }

  .brand-name {
    position: absolute;
    font-weight: 400;
    white-space: nowrap;
  }
  .card--front .brand-name {
    left: 40px; top: 48px;
    font-size: 86px; color: var(--gold);
  }
  .tagline {
    position: absolute; left: 44px; top: 168px;
    font-size: 21px; letter-spacing: 1px;
    color: var(--ink-grey); text-transform: uppercase;
  }
  .contact {
    position: absolute; left: 44px; bottom: 34px; right: 40px;
    display: flex; justify-content: space-between;
    font-size: 20px; color: var(--light);
    letter-spacing: 1px; text-transform: uppercase;
  }

  .card--back .brand-name {
    right: 50px; top: 120px;
    font-size: 96px; color: var(--light);
  }
  .web-address {
    position: absolute; left: 250px; top: 250px;
    font-size: 26px; color: var(--light); letter-spacing: 1px;
  }
</style>
</head>
<body>
  <section class="card card--front">
    <div class="brand-name">Shaker Barons</div>
    <p class="tagline">Drinks that are sexy, sophisticated and delicious</p>
    <div class="bar-photo" role="img" aria-label="Photo of a mint cocktail on a glossy bar counter with warm red lights"></div>
    <div class="contact">
      <span>0491570156 or 0491570158</span>
      <span>info@shakerbarons.net</span>
    </div>
  </section>

  <section class="card card--back">
    <div class="bar-photo" role="img" aria-label="Photo of a mint cocktail on a bar counter with blurred bar lights behind"></div>
    <div class="brand-name">Shaker Barons</div>
    <div class="web-address">www.shakerbarons.net</div>
  </section>
</body>
</html>
```